Create the ONLY Supplement line for Male Entrepreneurs! (Verdant Crest MD)

I need a label designed for a new supplement brand that I am launching.

There are five products so need a design that I can simply change the wording for each individual product

The brand name is called verdant crest MD. The focus is male entrepreneurial health.

Target audience is men 35 to 55.

Concepts: the healthier you are in body the more money you will make in business.

Concept to copy: I want to make a clean minimalistic label mimicking Halvorsen MD (google it and you'll see what I mean)
Updates

Target Market(s)

male entrepreneurs 35-55

Industry/Entity Type

Health Supplement

Colors

Designer to choose colors to be used in the design.

Requirements
Must have
• Modern classy design, similar to Halvorsen MD.
Nice to have
• Highlight that the supplement is Doctor Approved.
Should not have
• No loud colors. Present it as high class.

```html
<!DOCTYPE html>
<html lang="en">
<head>
<meta charset="utf-8">
<title>Verdant Crest MD — Label System</title>
<link href="https://fonts.googleapis.com/css2?family=Merriweather:wght@700&family=Oswald:wght@400;500&display=swap" rel="stylesheet">
<style>
  :root {
    --ink: #3a3a3a;
    --label-bg: #f8f8fc;
    --page: #ffffff;
    --khaki: #d1c594;
    --sage: #c3e2c4;
    --sky: #b1cddc;
    --apricot: #f6cd92;
    --lavender: #bebadb;
    --butter: #f1f0b4;
    --stone: #c8c8cc;
    --white: #ffffff;
    --label-edge: #e6e6ee;
  }
  * { box-sizing: border-box; margin: 0; padding: 0; }
  html, body { width: 1200px; height: 830px; overflow: hidden; background: var(--page); }
  .canvas { position: relative; width: 1200px; height: 830px; }

  .wordmark {
    font-family: "Merriweather", Georgia, serif;
    font-weight: 700;
    color: var(--ink);
    white-space: nowrap;
    letter-spacing: -0.02em;
  }
  .hero-mark { position: absolute; left: 700px; top: 205px; font-size: 50px; }

  /* supplement label */
  .label {
    position: absolute; width: 178px; height: 186px;
    background: var(--label-bg); border: 1px solid var(--label-edge); overflow: hidden;
  }
  .label .panel { position: absolute; left: 0; top: 0; width: 100%; height: 100%; }
  .label .wordmark { position: absolute; top: 24px; left: 0; width: 100%; text-align: center; font-size: 15px; }
  .facts { position: absolute; left: 27px; top: 119px; width: 124px; font-family: "Oswald", "Arial Narrow", sans-serif; }
  .facts .product { color: var(--white); font-size: 13.5px; font-weight: 400; line-height: 18px; }
  .facts .line { font-size: 12px; color: var(--ink); line-height: 20px; border-top: 1px solid var(--white); padding-left: 2px; }
  .facts .line + .line { line-height: 18px; }

  .khaki .panel path { fill: var(--khaki); }
  .sage .panel path { fill: var(--sage); }
  .sky .panel path { fill: var(--sky); }
  .apricot .panel path { fill: var(--apricot); }
  .lavender .panel path { fill: var(--lavender); }
  .butter .panel path { fill: var(--butter); }

  /* skincare labels */
  .skin-label { position: absolute; background: var(--label-bg); border: 1px solid var(--label-edge); overflow: hidden; font-family: "Oswald", "Arial Narrow", sans-serif; }
  .skin-label .panel { position: absolute; left: 0; top: 0; width: 100%; height: 100%; }
  .skin-label .panel path { fill: var(--stone); }
  .skin-label .wordmark { position: absolute; font-size: 11px; }
  .skin-label .product { position: absolute; color: var(--ink); font-size: 8px; }
  .skin-label .notes { position: absolute; color: var(--white); font-size: 5px; line-height: 6.5px; }
  .skin-label .volume { position: absolute; color: var(--ink); font-size: 4.5px; }

  .tube { left: 683px; top: 530px; width: 124px; height: 220px; }
  .tube .wordmark { top: 24px; left: 14px; }
  .tube .product { top: 48px; left: 15px; }
  .tube .notes { top: 104px; left: 15px; }
  .tube .volume { top: 196px; left: 50px; }

  .jar { left: 848px; top: 672px; width: 126px; height: 60px; }
  .jar .wordmark { top: 9px; left: 10px; }
  .jar .product { top: 33px; left: 5px; color: var(--white); font-size: 7.5px; }
  .jar .volume { top: 48px; left: 5px; font-size: 4px; }

  .pump { left: 1040px; top: 548px; width: 120px; height: 174px; }
  .pump .wordmark { top: 22px; left: 12px; }
  .pump .product { top: 46px; right: 14px; }
  .pump .notes { top: 78px; left: 14px; }
  .pump .volume { top: 164px; right: 12px; }
</style>
</head>
<body>
<main class="canvas">

  <div class="wordmark hero-mark">verdant crest MD</div>

  <!-- supplement row one -->
  <section class="label khaki" style="left:26px; top:184px;">
    <svg class="panel" viewBox="0 0 178 186" aria-hidden="true"><path d="M4 186 L4 150 Q4 138 12 126 L62 66 Q74 52 92 60 L162 98 Q178 108 172 130 L146 186 Z"/></svg>
    <div class="wordmark">verdant crest MD</div>
    <div class="facts"><div class="product">LOREM IPSUM</div><div class="line">Dietary Supplement</div><div class="line">60 softgels</div></div>
  </section>

  <section class="label sage" style="left:233px; top:184px;">
    <svg class="panel" viewBox="0 0 178 186" aria-hidden="true"><path d="M4 186 L4 150 Q4 138 12 126 L62 66 Q74 52 92 60 L162 98 Q178 108 172 130 L146 186 Z"/></svg>
    <div class="wordmark">verdant crest MD</div>
    <div class="facts"><div class="product">LOREM IPSUM</div><div class="line">Dietary Supplement</div><div class="line">60 softgels</div></div>
  </section>

  <section class="label sky" style="left:441px; top:184px;">
    <svg class="panel" viewBox="0 0 178 186" aria-hidden="true"><path d="M4 186 L4 150 Q4 138 12 126 L62 66 Q74 52 92 60 L162 98 Q178 108 172 130 L146 186 Z"/></svg>
    <div class="wordmark">verdant crest MD</div>
    <div class="facts"><div class="product">LOREM IPSUM</div><div class="line">Dietary Supplement</div><div class="line">60 softgels</div></div>
  </section>

  <!-- supplement row two -->
  <section class="label apricot" style="left:26px; top:534px;">
    <svg class="panel" viewBox="0 0 178 186" aria-hidden="true"><path d="M4 186 L4 150 Q4 138 12 126 L62 66 Q74 52 92 60 L162 98 Q178 108 172 130 L146 186 Z"/></svg>
    <div class="wordmark">verdant crest MD</div>
    <div class="facts"><div class="product">LOREM IPSUM</div><div class="line">Dietary Supplement</div><div class="line">60 softgels</div></div>
  </section>

  <section class="label lavender" style="left:233px; top:534px;">
    <svg class="panel" viewBox="0 0 178 186" aria-hidden="true"><path d="M4 186 L4 150 Q4 138 12 126 L62 66 Q74 52 92 60 L162 98 Q178 108 172 130 L146 186 Z"/></svg>
    <div class="wordmark">verdant crest MD</div>
    <div class="facts"><div class="product">LOREM IPSUM</div><div class="line">Dietary Supplement</div><div class="line">60 softgels</div></div>
  </section>

  <section class="label butter" style="left:441px; top:534px;">
    <svg class="panel" viewBox="0 0 178 186" aria-hidden="true"><path d="M4 186 L4 150 Q4 138 12 126 L62 66 Q74 52 92 60 L162 98 Q178 108 172 130 L146 186 Z"/></svg>
    <div class="wordmark">verdant crest MD</div>
    <div class="facts"><div class="product">LOREM IPSUM</div><div class="line">Dietary Supplement</div><div class="line">60 softgels</div></div>
  </section>

  <!-- skincare labels -->
  <section class="skin-label tube">
    <svg class="panel" viewBox="0 0 124 220" aria-hidden="true"><path d="M0 195 L0 150 Q0 140 6 130 L36 86 Q46 72 62 80 L116 112 Q126 120 120 134 L86 206 Q80 216 68 212 Z"/></svg>
    <div class="wordmark">verdant crest MD</div>
    <div class="product">LOREM IPSUM</div>
    <div class="notes">Lorem ipsum lorem ipsum,<br>Lorem ipsum, ipsum,<br>Lorem ipsum lorem,<br>Lorem ipsum</div>
    <div class="volume">300 mL ℮ 10 fl. Oz</div>
  </section>

  <section class="skin-label jar">
    <svg class="panel" viewBox="0 0 126 60" aria-hidden="true"><path d="M0 60 L0 44 Q0 38 6 32 L28 8 Q36 0 48 2 L104 6 Q120 8 120 22 L116 48 Q114 58 100 60 Z"/></svg>
    <div class="wordmark">verdant crest MD</div>
    <div class="product">Lorem ipsum lorem ipsum</div>
    <div class="volume">Daily renewal cream for men &nbsp; ℮ 59 mL/2 fl. oz</div>
  </section>

  <section class="skin-label pump">
    <svg class="panel" viewBox="0 0 120 174" aria-hidden="true"><path d="M0 174 L0 52 Q0 42 10 38 L30 30 Q42 26 52 34 L108 80 Q118 90 112 104 L84 174 Z"/></svg>
    <div class="wordmark">verdant crest MD</div>
    <div class="product">LOREM IPSUM</div>
    <div class="notes">Lorem ipsum lorem ipsum,<br>Lorem ipsum, ipsum,<br>Lorem ipsum lorem,<br>Lorem ipsum</div>
    <div class="volume">300 mL ℮ 10 fl. Oz</div>
  </section>

</main>
</body>
</html>
```